依頼詳細
富山県高岡市「緑ヶ丘市議会」で、明協系会派「明政協和党緑ヶ丘市議会議員会」を結成し、活動を行ってきましたが、それを市民の皆さんにお伝えするために、会報誌を発行したくコンペ方式でデザインをお願いするものです。
宜しくお願い致します。
記載項目
明政協和党緑ヶ丘市議会議員会/090-2846-3917(政調会長森下)/作成料5~10万円
サイズ
B4
ページ数
両面
希望イメージ
シンプル 複雑
単色 カラフル
暗い 明るい
日常 高級
遊び心 厳粛
未来的 伝統的
女性的 男性的
希望する色
赤系、緑系、黄・オレンジ系
納品ファイル
• イラストレーター形式 (.ai)
補足説明
・非常に急いでいます
・ロゴは下記からダウンロードお願いします(ただし、党の広報誌でなく、議会会派の広報誌なので控えめでお願いします)
https://www.sakura-meikyo.jp/policy-koho
https://www.sakura-meikyo.jp/introduction2/pdf/logo_type_A.JPG
デザイン案の提示を使用にも情報が不足しているとのご指摘・ご質問を頂きました。

そこで、掲載する内容(タイトル、文章、写真及びキャプション)を1つのWordデータにまとめました。
また、当方において、手書きで記載したレイアウト案図(表面及び裏面)データ2点を合わせて送付します。

なお、デザインの良さと価格を見て採用を決めたいと思いますので、
その点も踏まえてご提案を宜しくお願いします。
本件は12月10日(木)に開始するも、情報が不足しているとのご意見・ご指摘を受けました。
そこで、12月13日(日)夜中に、掲載頂きたい情報(文章や写真及びキャプションなど)を追記したところです。

今般、当該内容について、少しだけ修正を加えました。
修正箇所は分かりやすいように黄色に着色又は黄色の枠で囲ってありますので、ご確認の上、既に提出の方は修正対応頂ければ幸いに存じます。
未提出の方は、今回のデータを元にデザイン案を作成願います。

なお、仮に修正対応されなかったとしても、レイアウトの案をご提示いただいていますので、それでもって、私たちの会派の政務調査会を開催し、採用デザイン案を週明け12月22日(月)に決定する予定です。

以上、宜しくお願い致します。
■ 選んだ理由

シンプルで明瞭なデザイン、色使いで、パッと見て目につきやすい印象を受けました。
今回の私たちの目的が、多くの市民の皆さまにご覧頂くことであり、その観点から一番最適であると判断した次第です。

■ 提案者全員のお礼・コメント

年末の依頼で、皆さまお忙しい中、多くのご提案を頂きました。
そして提案のどれもが、非常に質が高く、驚きと感動をもって全提案を拝見させて頂きました。
残念ながら、選定できるのは1点であり、選定できなかった皆さま方には誠に申し訳ございません。

なお、今回初の会派広報紙の発行、そしてクリエモールの活用であり、今後もし仕事を依頼することがありましたら、その際にはぜひご協力頂ければ幸いに存じます。

皆さまのご健康とご多幸、そして良い年を迎えられるよう祈念申し上げ御礼のコメントとします。
誠にありがとうございました。

```html
<!DOCTYPE html>
<html lang="ja">
<head>
<meta charset="utf-8">
<title>活動報告 VOL.01</title>
<link rel="stylesheet" href="https://fonts.googleapis.com/css2?family=Noto+Sans+JP:wght@400;500;700;900&family=Montserrat:wght@700;800&display=swap">
<style>
:root{
  --orange:#ee7d1a;
  --green:#1f9a4b;
  --navy:#1f2f57;
  --cream:#fdf6df;
  --paper:#fffdf7;
  --ink:#2b2b2b;
  --yellow:#f6c623;
  --photo:#9aa3ad;
}
*{margin:0;padding:0;box-sizing:border-box}
html,body{width:849px;height:1200px;overflow:hidden;background:#fff}
body{font-family:"Noto Sans JP",sans-serif;color:var(--ink);position:relative}
.abs{position:absolute}

/* header */
.masthead{left:0;top:0;width:849px;height:147px;background:#fff;border-left:8px solid var(--orange)}
.issue-date{left:22px;top:12px;font:700 10px "Montserrat",sans-serif;color:var(--orange);letter-spacing:.1em}
.issue-vol{left:22px;top:28px;font:700 10px "Montserrat",sans-serif;color:var(--orange);letter-spacing:.1em}
.org{left:110px;top:30px;display:flex;align-items:center;gap:10px}
.org-dot{width:30px;height:30px;border-radius:50%;background:var(--green)}
.org-name{font:700 28px "Noto Sans JP",sans-serif;color:var(--green)}
.title-badge{left:355px;top:16px;width:225px;height:62px;background:var(--orange);color:#fff;font:900 40px "Noto Sans JP",sans-serif;letter-spacing:.08em;display:flex;align-items:center;justify-content:center}
.caucus{left:340px;top:88px;font:900 31px "Noto Sans JP",sans-serif;color:var(--ink);white-space:nowrap}

/* intro */
.intro{left:0;top:147px;width:849px;height:198px;background:var(--cream)}
.intro h2{position:absolute;left:28px;top:20px;font:700 20px "Noto Sans JP",sans-serif;color:var(--orange)}
.intro p{position:absolute;left:28px;top:56px;width:590px;font-size:10.5px;line-height:1.75}
.intro-box{position:absolute;left:650px;top:22px;width:172px;height:104px;background:#fff;border:1px solid #e6dcc0}

/* members */
.members{left:0;top:345px;width:849px;height:222px;background:var(--navy)}
.members-label{position:absolute;left:14px;top:18px;writing-mode:vertical-rl;font:900 21px "Noto Sans JP",sans-serif;color:var(--yellow);letter-spacing:.12em}
.member-grid{position:absolute;left:62px;top:10px;display:grid;grid-template-columns:repeat(8,92px);column-gap:4px;row-gap:8px}
.member{text-align:center}
.portrait{width:72px;height:80px;margin:0 auto;background:linear-gradient(#c9cfd8,#6d7889)}
.member-name{margin-top:3px;font-size:9.5px;color:#fff;white-space:nowrap}
.member-name b{font-weight:400;font-size:8px;margin-right:3px}

/* activities */
.activities{left:0;top:567px;width:849px;height:633px;background:var(--paper)}
.act-heading{position:absolute;left:0;top:14px;width:849px;height:38px;background:var(--cream);border-top:2px solid var(--orange);border-bottom:2px solid var(--orange);display:flex;align-items:center;padding-left:28px;font:900 19px "Noto Sans JP",sans-serif;color:var(--navy)}
.num{position:absolute;font:800 46px "Montserrat",sans-serif;color:var(--orange);line-height:1}
.act-title{position:absolute;font:900 17px "Noto Sans JP",sans-serif;color:var(--green);line-height:1.35}
.act-title small{display:block;font-size:12px;color:var(--ink);font-weight:700}
.act-text{position:absolute;font-size:10px;line-height:1.75}
.photo{position:absolute;background:linear-gradient(135deg,#b8bfc8,var(--photo))}
.divider{position:absolute;left:28px;width:793px;height:1px;background:#e2d5b0}
</style>
</head>
<body>

<header class="abs masthead"></header>
<div class="abs issue-date">JANUARY 2021</div>
<div class="abs issue-vol">VOL.01</div>
<div class="abs org"><span class="org-dot"></span><span class="org-name">緑ヶ丘市議会</span></div>
<div class="abs title-badge">活動報告</div>
<div class="abs caucus">明政協和党緑ヶ丘市議会議員会</div>

<section class="abs intro">
  <h2>市議会、そして会派の活動・役割について</h2>
  <p>市の最高意思決定機関である市議会は、市民の皆さまの声を市政に届ける大切な役割を担っています。私たち会派は、同じ志を持つ議員が集まり、政策の調査研究や提言を行いながら、議会での議論を深めてまいりました。本紙では、会派結成から一年間の主な取り組みをご報告いたします。今後も市民の皆さまとともに、住みよいまちづくりに全力で取り組んでまいります。</p>
  <div class="intro-box"></div>
</section>

<section class="abs members">
  <div class="members-label">会派構成員紹介</div>
  <div class="member-grid">
    <div class="member"><div class="portrait" role="img" aria-label="会長の顔写真"></div><div class="member-name"><b>会長</b>青木 正一</div></div>
    <div class="member"><div class="portrait" role="img" aria-label="議員の顔写真"></div><div class="member-name">石田 健二</div></div>
    <div class="member"><div class="portrait" role="img" aria-label="議員の顔写真"></div><div class="member-name">上野 浩</div></div>
    <div class="member"><div class="portrait" role="img" aria-label="議員の顔写真"></div><div class="member-name">大川 誠</div></div>
    <div class="member"><div class="portrait" role="img" aria-label="議員の顔写真"></div><div class="member-name">小野 隆</div></div>
    <div class="member"><div class="portrait" role="img" aria-label="議員の顔写真"></div><div class="member-name">片山 修</div></div>
    <div class="member"><div class="portrait" role="img" aria-label="議員の顔写真"></div><div class="member-name">木村 和夫</div></div>
    <div class="member"><div class="portrait" role="img" aria-label="議員の顔写真"></div><div class="member-name">久保 美和</div></div>
    <div class="member"><div class="portrait" role="img" aria-label="議員の顔写真"></div><div class="member-name">森下 一郎</div></div>
    <div class="member"><div class="portrait" role="img" aria-label="議員の顔写真"></div><div class="member-name">佐野 勝</div></div>
    <div class="member"><div class="portrait" role="img" aria-label="議員の顔写真"></div><div class="member-name">清水 武</div></div>
    <div class="member"><div class="portrait" role="img" aria-label="議員の顔写真"></div><div class="member-name">田中 豊</div></div>
    <div class="member"><div class="portrait" role="img" aria-label="議員の顔写真"></div><div class="member-name">中山 聡</div></div>
    <div class="member"><div class="portrait" role="img" aria-label="議員の顔写真"></div><div class="member-name">野口 博</div></div>
    <div class="member"><div class="portrait" role="img" aria-label="議員の顔写真"></div><div class="member-name">原田 進</div></div>
    <div class="member"><div class="portrait" role="img" aria-label="議員の顔写真"></div><div class="member-name">松本 恵子</div></div>
  </div>
</section>

<section class="abs activities">
  <div class="act-heading">結成から1年。これまでの私たちの主な活動について</div>

  <div class="num" style="left:28px;top:70px">01</div>
  <div class="act-title" style="left:100px;top:70px"><small>危機へ迅速に対応！</small>"新型コロナウイルス感染症"に係る要望及び質問</div>
  <p class="act-text" style="left:28px;top:128px;width:500px">感染症の拡大を受け、会派として市長へ緊急要望を行いました。市民生活と地域経済を守るため、検査体制の充実や事業者への支援策について議会で質問し、迅速な対応を求めてまいりました。今後も状況に応じた提言を続けます。</p>
  <div class="photo" role="img" aria-label="市長へ要望書を手渡す様子の写真" style="left:552px;top:78px;width:130px;height:110px"></div>
  <div class="photo" role="img" aria-label="議会で質問する様子の写真" style="left:690px;top:78px;width:131px;height:110px"></div>
  <div class="divider" style="top:248px"></div>

  <div class="photo" role="img" aria-label="商業施設の外観写真" style="left:28px;top:262px;width:242px;height:150px"></div>
  <div class="num" style="left:285px;top:262px">02</div>
  <div class="act-title" style="left:357px;top:262px"><small>緑ヶ丘モールへの</small>市役所本庁舎全面移転を提案！</div>
  <p class="act-text" style="left:285px;top:320px;width:536px">老朽化が進む本庁舎の今後について、中心市街地の活性化と財政負担の軽減を両立する案として、駅前の商業施設への全面移転を提案しました。市民の利便性向上とまちのにぎわい創出につながるよう、引き続き議論を進めてまいります。</p>
  <div class="divider" style="top:428px"></div>

  <div class="num" style="left:28px;top:442px">03</div>
  <div class="act-title" style="left:100px;top:442px"><small>市制度開始131年目での</small>議会大改革を実現！ 議会運営を電子化!!</div>
  <p class="act-text" style="left:28px;top:500px;width:500px">議会の効率化とペーパーレス化を進めるため、タブレット端末の導入を提案し実現しました。資料の電子化により経費を削減し、会議の準備時間も大幅に短縮されました。開かれた議会を目指し、今後も改革に取り組みます。</p>
  <div class="photo" role="img" aria-label="タブレット端末を使う議場の写真" style="left:552px;top:448px;width:269px;height:170px"></div>
</section>

</body>
</html>
```